agricultural technology company needs business cards*

design a business card that represents our business well. please see our website: halverstonfieldguard.com.au
professional, simple, clean lines, not complicated or floral.....

```html
<!DOCTYPE html>
<html lang="en">
<head>
<meta charset="utf-8">
<title>Halverston FieldGuard – Business Card</title>
<link rel="stylesheet" href="https://fonts.googleapis.com/css2?family=Lato:wght@400;700&display=swap">
<style>
  :root {
    --stage: #e7e3dc;
    --card-dark: #25262a;
    --card-light: #f8f8f8;
    --green: #2bb24c;
    --lime: #9fcd3a;
    --navy: #1f2a5c;
    --ink: #333333;
    --white: #ffffff;
  }
  * { margin: 0; padding: 0; box-sizing: border-box; }
  html, body {
    width: 1200px;
    height: 896px;
    overflow: hidden;
    background: var(--stage);
    font-family: "Lato", sans-serif;
  }
  .stage { position: relative; width: 1200px; height: 896px; }
  .card {
    position: absolute;
    left: 302px;
    width: 619px;
    height: 354px;
    box-shadow: 0 6px 18px rgba(0,0,0,0.18);
  }
  .card--front { top: 95px; background: var(--card-dark); }
  .card--back { top: 469px; background: var(--card-light); }

  .brand {
    position: absolute;
    display: flex;
    align-items: flex-start;
    gap: 10px;
  }
  .brand__name {
    font-weight: 700;
    color: var(--green);
    line-height: 0.95;
    letter-spacing: -0.01em;
  }
  .brand__square { background: var(--lime); flex: none; }

  .card--front .brand { left: 42px; top: 222px; }
  .card--front .brand__name { font-size: 38px; color: var(--white); }
  .card--front .brand__square { width: 20px; height: 20px; margin-top: 8px; }

  .card--back .brand { left: 35px; top: 40px; }
  .card--back .brand__name { font-size: 22px; color: var(--green); }
  .card--back .brand__square { width: 12px; height: 12px; margin-top: 5px; }

  .contact { position: absolute; left: 35px; top: 148px; color: var(--ink); }
  .contact__name { font-size: 19px; font-weight: 700; color: var(--navy); line-height: 1.2; }
  .contact__role { font-size: 14px; line-height: 1.3; margin-bottom: 14px; }
  .contact__address { font-size: 14px; line-height: 1.5; margin-bottom: 12px; }
  .contact__list { list-style: none; font-size: 14px; line-height: 1.35; }
  .contact__list li { display: flex; align-items: center; gap: 7px; }
  .contact__list svg { width: 11px; height: 11px; flex: none; fill: var(--green); }
</style>
</head>
<body>
<main class="stage">
  <section class="card card--front" aria-label="Card front">
    <div class="brand">
      <p class="brand__name">Halverston<br>FieldGuard</p>
      <span class="brand__square" aria-hidden="true"></span>
    </div>
  </section>

  <section class="card card--back" aria-label="Card back">
    <div class="brand">
      <p class="brand__name">Halverston<br>FieldGuard</p>
      <span class="brand__square" aria-hidden="true"></span>
    </div>
    <div class="contact">
      <p class="contact__name">Marten Du Plessis</p>
      <p class="contact__role">Director</p>
      <p class="contact__address">14 Bellamy Road<br>Baldivis, WA 6171</p>
      <ul class="contact__list">
        <li>
          <svg viewBox="0 0 24 24" aria-hidden="true"><path d="M6.6 10.8a15.1 15.1 0 0 0 6.6 6.6l2.2-2.2a1 1 0 0 1 1-.25 11.4 11.4 0 0 0 3.6.57 1 1 0 0 1 1 1V20a1 1 0 0 1-1 1A17 17 0 0 1 3 4a1 1 0 0 1 1-1h3.5a1 1 0 0 1 1 1c0 1.25.2 2.45.57 3.57a1 1 0 0 1-.25 1z"/></svg>
          1300 482 316
        </li>
        <li>
          <svg viewBox="0 0 24 24" aria-hidden="true"><path d="M2 5h20v14H2z M2 5l10 8 10-8" /></svg>
          halverstonfieldguard@com.au
        </li>
        <li>
          <svg viewBox="0 0 24 24" aria-hidden="true"><circle cx="12" cy="12" r="10"/></svg>
          halverstonfieldguard.com.au
        </li>
      </ul>
    </div>
  </section>
</main>
</body>
</html>
```